A Freight forwarding (transportation/shipping) company requires stationary designs

We need The following:
1. Letterhead
2. Letter Envelope
3. Business Card Design
4. A4 Paper Envelope
5. A4 Paper Folder (One that is 2xA4 foldable size which we can open in half and we can put a paper in between and has a lot for business card)
6. A5 Paper (To be used for notes taking)
a design for a freight forwarding company named KORVELA MIND INTERNATIONAL TRANSPORTATION.
(We are active in Sea Transportation, Truck transportation, and Air Transportation, (printed design in PDF is required with all open source files for editing - lamination accepted)
Playing around with the Logo is accepted,, Korvela Logo.png is the correct logo.
Example of folder, envelopes, and notepad attached
Address of the company is :
No 7, 4th Tarandil Gharbi, Neshat Lar Blvd,
Mashhad, IR
Tel : +98 51 37412958
Fax : +98 51 37490316
Website : www.korvela-example.com
Email : info@korvela-example.com

```html
<!DOCTYPE html>
<html lang="en">
<head>
<meta charset="utf-8">
<title>Korvela Mind Letterhead</title>
<link href="https://fonts.googleapis.com/css2?family=Arimo:wght@400;700&display=swap" rel="stylesheet">
<style>
  :root {
    --navy: #3a4589;
    --green: #2f9242;
    --rule: #2e9a3e;
    --ink: #1d1d1b;
    --paper: #ffffff;
    --edge: #c8c8c8;
  }
  html, body { margin: 0; padding: 0; overflow: hidden; background: var(--paper); }
  .letterhead {
    position: relative;
    width: 839px;
    height: 1200px;
    box-sizing: border-box;
    border: 1px solid var(--edge);
    background: var(--paper);
    overflow: hidden;
    font-family: "Arimo", Arial, sans-serif;
  }
  .brand {
    position: absolute;
    top: 40px;
    left: 664px;
    width: 142px;
    text-align: center;
    color: var(--ink);
  }
  .brand-mark {
    display: block;
    width: 104px;
    height: 104px;
    margin: 0 auto 14px;
    border-radius: 50%;
    border: 8px solid var(--navy);
    box-sizing: border-box;
  }
  .brand-name {
    margin: 0;
    font-size: 16px;
    font-weight: 400;
    letter-spacing: -0.2px;
    line-height: 1;
  }
  .brand-tagline {
    margin: 3px 0 0;
    font-size: 7.4px;
    font-weight: 400;
    line-height: 1;
  }
  .writing-lines {
    position: absolute;
    left: 39px;
    top: 0;
    width: 759px;
    height: 1200px;
  }
  .footer-wave {
    position: absolute;
    left: 0;
    bottom: 0;
    width: 839px;
    height: 201px;
  }
  .contact {
    position: absolute;
    color: #fff;
    font-size: 14px;
    font-weight: 700;
    line-height: 20px;
    margin: 0;
  }
  .contact-web { left: 40px; top: 1115px; }
  .contact-phone { left: 328px; top: 1115px; }
  .contact-address { right: 43px; top: 1117px; text-align: right; }
  .contact-address .label { margin-right: 2px; }
</style>
</head>
<body>
<div class="letterhead">
  <div class="brand">
    <span class="brand-mark"></span>
    <p class="brand-name">KORVELA MIND</p>
    <p class="brand-tagline">International Transportation</p>
  </div>

  <svg class="writing-lines" viewBox="0 0 759 1200" aria-hidden="true">
    <g stroke="var(--rule)" stroke-width="2.6">
      <line x1="0" x2="759" y1="222" y2="222"/>
      <line x1="0" x2="759" y1="274" y2="274"/>
      <line x1="0" x2="759" y1="326" y2="326"/>
      <line x1="0" x2="759" y1="378" y2="378"/>
      <line x1="0" x2="759" y1="430" y2="430"/>
      <line x1="0" x2="759" y1="482" y2="482"/>
      <line x1="0" x2="759" y1="534" y2="534"/>
      <line x1="0" x2="759" y1="586" y2="586"/>
      <line x1="0" x2="759" y1="638" y2="638"/>
      <line x1="0" x2="759" y1="690" y2="690"/>
      <line x1="0" x2="759" y1="742" y2="742"/>
      <line x1="0" x2="759" y1="794" y2="794"/>
      <line x1="0" x2="759" y1="846" y2="846"/>
      <line x1="0" x2="759" y1="898" y2="898"/>
      <line x1="0" x2="759" y1="950" y2="950"/>
      <line x1="0" x2="759" y1="997" y2="997"/>
    </g>
  </svg>

  <svg class="footer-wave" viewBox="0 1190 1000 240" preserveAspectRatio="none" aria-hidden="true">
    <path d="M0,1225 C10,1300 110,1395 300,1430 L0,1430 Z" fill="var(--green)"/>
    <path d="M8,1240 C30,1300 80,1340 160,1380" stroke="#fff" stroke-width="5" fill="none"/>
    <path d="M33,1200 C120,1290 230,1335 400,1305 C560,1275 700,1218 820,1222 C900,1225 960,1245 1000,1262 L1000,1430 L290,1430 C160,1405 70,1375 33,1335 Z" fill="var(--navy)"/>
    <path d="M1000,1288 C940,1325 925,1375 955,1430 L1000,1430 Z" fill="var(--green)"/>
    <path d="M1000,1345 C975,1370 970,1400 985,1430 L1000,1430 Z" fill="var(--navy)"/>
  </svg>

  <p class="contact contact-web">E &nbsp;| info@korvela-example.com<br>W | www.korvela-example.com</p>
  <p class="contact contact-phone">T | + 98 51 37412958<br>F | + 98 51 37490316</p>
  <p class="contact contact-address"><span class="label">A |</span> No 7, 4th Tarandil Gharbi,<br>Neshat Lar Blvd, Mashhad, IR</p>
</div>
</body>
</html>
```